Pharmacy ad

need 2 pharmacy ads for the phone book. one for Birchfield Pharmacy and one for Corvane Rx Pharmacy. Dimensions for ad is 4.75in x 4.667 in. please see attached examples of ad uploaded as well logos of each pharmacy

```html
<!DOCTYPE html>
<html lang="en">
<head>
<meta charset="utf-8">
<title>Pharmacy phone book ads</title>
<link rel="stylesheet" href="https://fonts.googleapis.com/css2?family=Montserrat:wght@400;500;600;700;800&family=Roboto+Condensed:wght@300;400;700;900&family=Kaushan+Script&display=swap">
<style>
  :root{
    --page:#fcef9f;
    --navy:#1d2552;
    --blue:#2e4ba0;
    --green:#7cbf43;
    --green-soft:#c9e19b;
    --green-pale:#dcebb5;
    --sky:#a7d5ea;
    --sky-pale:#e3f2f8;
    --white:#ffffff;
    --ink:#1a1a1a;
  }
  *{box-sizing:border-box;margin:0;padding:0}
  html,body{width:1200px;height:600px;overflow:hidden;background:var(--page)}
  .canvas{position:relative;width:1200px;height:600px;background:var(--page);overflow:hidden}

  /* ---------- Birchfield ad ---------- */
  .ad{position:absolute;width:569px;height:557px;overflow:hidden}
  .ad--birchfield{left:19px;top:21px;border:2px solid var(--navy);font-family:"Montserrat",sans-serif;color:var(--navy);background:var(--white)}
  .ad--birchfield .backdrop{position:absolute;inset:0}
  .discounts{position:absolute;left:22px;top:12px;width:250px;text-align:center}
  .discount__rate{font-weight:800;font-size:40px;line-height:38px;letter-spacing:-1px}
  .discount__label{font-weight:400;font-size:14.5px;line-height:16px}
  .discount__detail{font-weight:700;font-size:13px;line-height:14px}
  .discount__rule{border-top:3px dotted var(--navy);margin:8px 12px 6px}
  .brand{position:absolute;left:300px;top:60px;width:255px;text-align:center}
  .brand__mark{width:78px;height:78px;border-radius:50%;background:var(--green);margin:0 auto 14px}
  .brand__name{font-weight:700;font-size:34px;line-height:36px;letter-spacing:.5px;color:var(--navy)}
  .brand__tagline{font-weight:500;font-size:13px;color:var(--green);margin-top:10px}
  .payments{position:absolute;left:368px;top:326px;width:180px;display:flex;flex-wrap:wrap;gap:8px;justify-content:center}
  .payment{background:var(--white);color:var(--navy);font-weight:700;font-size:11px;padding:7px 6px;min-width:50px;text-align:center}
  .services{position:absolute;left:34px;top:304px;display:flex;gap:8px;font-weight:700;font-size:12px;line-height:13.5px;color:var(--ink)}
  .services ul{list-style:none}
  .services li{position:relative;padding-left:11px;margin-bottom:5px}
  .services li::before{content:"";position:absolute;left:0;top:4px;width:5px;height:5px;background:var(--ink);transform:rotate(45deg)}
  .services .col-a{width:150px}
  .services .col-b{width:120px}
  .footer-rule{position:absolute;left:24px;top:414px;width:390px;border-top:3px dotted var(--navy)}
  .inquiry{position:absolute;left:26px;top:428px;font-size:13.5px;font-weight:500;color:var(--ink)}
  .locations{position:absolute;left:26px;top:460px;display:flex;color:var(--ink)}
  .location{width:232px;font-size:11.5px;font-weight:700;line-height:13px}
  .location + .location{border-left:2px solid var(--ink);padding-left:8px;width:210px}
  .location small{display:block;font-weight:400;font-size:10px}
  .location .line{display:flex;align-items:flex-start;gap:5px;margin-bottom:3px}
  .location svg{flex:none;margin-top:1px}
  .location .hours{font-size:12.5px;line-height:14px;margin-top:6px}
  .social{position:absolute;left:476px;top:462px;width:74px;text-align:center;font-size:12px;color:var(--ink)}
  .social__dot{width:46px;height:46px;border-radius:50%;background:var(--blue);margin:6px auto 3px}
  .social__name{font-size:11px;font-weight:600;color:var(--blue);line-height:13px}

  /* ---------- Corvane ad ---------- */
  .ad--corvane{left:610px;top:22px;border:2px solid var(--green);font-family:"Roboto Condensed",sans-serif;background:var(--white);color:var(--blue)}
  .hero{position:absolute;left:0;top:0;width:100%;height:226px;background:linear-gradient(90deg,#f4f5f5 0%,#e9edee 45%,#cfd8da 70%,#9c8f86 100%)}
  .cv-brand{position:absolute;left:36px;top:58px;display:flex;align-items:center;gap:14px}
  .cv-brand__mark{width:44px;height:44px;background:var(--green)}
  .cv-brand__name{font-weight:700;font-size:38px;line-height:38px;color:var(--blue)}
  .cv-brand__sub{font-weight:700;font-size:19px;letter-spacing:1px;color:var(--blue);border-top:2px solid var(--green);margin-top:4px;padding-top:2px;text-align:center}
  .accept{position:absolute;left:78px;top:128px}
  .accept__title{font-weight:700;font-size:13px;color:var(--ink);margin-bottom:4px}
  .accept__row{display:flex;gap:7px}
  .accept .payment{font-family:"Roboto Condensed",sans-serif;font-size:12px;border:1px solid #cfd6dc}
  .band{position:absolute;left:0;top:168px;width:100%;height:140px}
  .slogan{position:absolute;left:0;top:216px;width:100%;text-align:center;font-family:"Kaushan Script",cursive;font-size:44px;line-height:56px;color:var(--blue)}
  .cv-discounts{position:absolute;left:58px;top:302px}
  .cv-discount{display:flex;align-items:center;gap:6px;height:52px}
  .cv-discount__rate{font-weight:900;font-size:48px;line-height:48px;letter-spacing:-1px}
  .cv-discount__text{line-height:13px}
  .cv-discount__label{font-weight:300;font-size:22px;line-height:20px}
  .cv-discount__detail{font-weight:700;font-size:12.5px}
  .cv-divider{position:absolute;left:286px;top:312px;width:3px;height:142px;background:var(--green)}
  .cv-services{position:absolute;left:298px;top:318px;display:flex;gap:8px;font-size:13.5px;line-height:14px;color:var(--blue)}
  .cv-services ul{list-style:none}
  .cv-services li{position:relative;padding-left:10px;margin-bottom:11px}
  .cv-services li::before{content:"";position:absolute;left:0;top:5px;width:4px;height:4px;border-radius:50%;background:var(--blue)}
  .cv-services .col-a{width:134px}
  .cv-services .col-b{width:116px}
  .cv-footer{position:absolute;left:0;top:465px;width:100%;height:92px;background:var(--green);color:var(--ink)}
  .cv-contact{position:absolute;left:30px;top:8px;font-family:"Montserrat",sans-serif;font-weight:600;font-size:14px;line-height:22px}
  .cv-contact .line{display:flex;align-items:center;gap:8px}
  .cv-contact .gap{margin-left:22px}
  .cv-hours{font-weight:700;font-size:20px;margin-top:5px}
  .cv-social{position:absolute;left:478px;top:6px;width:76px;text-align:center;font-family:"Montserrat",sans-serif;font-size:12px;line-height:14px}
  .cv-social .social__dot{width:40px;height:40px;margin:4px auto 2px}
</style>
</head>
<body>
<div class="canvas">

  <!-- Birchfield Pharmacy ad -->
  <section class="ad ad--birchfield" aria-label="Birchfield Pharmacy advertisement">
    <svg class="backdrop" width="569" height="557" viewBox="0 0 569 557" aria-hidden="true">
      <defs>
        <linearGradient id="skyFade" x1="0" y1="0" x2="1" y2="0">
          <stop offset="0" stop-color="#9fd0e6"/>
          <stop offset=".45" stop-color="#cfe8f3"/>
          <stop offset=".6" stop-color="#f4fafc"/>
          <stop offset="1" stop-color="#ffffff"/>
        </linearGradient>
        <linearGradient id="meadow" x1="0" y1="0" x2="0" y2="1">
          <stop offset="0" stop-color="#b9d98a"/>
          <stop offset="1" stop-color="#d6e9ad"/>
        </linearGradient>
      </defs>
      <rect width="569" height="557" fill="url(#skyFade)" role="img" aria-label="Soft blurred pharmacy shelf background"/>
      <path d="M340 0 C250 120 260 300 420 420 C470 455 520 470 569 470 V0 Z" fill="#ffffff" opacity=".75"/>
      <path d="M330 282 C400 300 430 340 470 390 C500 430 540 455 569 460 V395 C520 390 480 360 440 320 C410 290 380 282 330 282 Z" fill="var(--sky)"/>
      <path d="M0 284 H300 C370 284 400 320 430 370 C465 430 510 470 569 480 V557 H0 Z" fill="url(#meadow)"/>
    </svg>

    <div class="discounts">
      <div class="discount__rate">10%</div>
      <div class="discount__label">SENIOR CITIZEN<br>DISCOUNT</div>
      <div class="discount__detail">FOR PATIENTS<br>60 YEARS AND OVER</div>
      <div class="discount__rule"></div>
      <div class="discount__rate">10%</div>
      <div class="discount__label">STUDENT DISCOUNT</div>
      <div class="discount__detail">WITH VALID ID CARD</div>
      <div class="discount__rule"></div>
      <div class="discount__rate">10%</div>
      <div class="discount__label">DISCOUNT ON HOSPITAL</div>
      <div class="discount__detail">PRESCRIPTIONS</div>
    </div>

    <div class="brand">
      <div class="brand__mark"></div>
      <div class="brand__name">BIRCHFIELD<br>PHARMACY</div>
      <div class="brand__tagline">We Care About Your Health</div>
    </div>

    <div class="payments">
      <span class="payment">Paylane</span>
      <span class="payment">Cardora</span>
      <span class="payment">Sagewell</span>
      <span class="payment">Nortide</span>
    </div>

    <div class="services">
      <ul class="col-a">
        <li>Certified Pharmacists</li>
        <li>Affordable prices</li>
        <li>Brand and Generic Medicines</li>
        <li>Blood Pressure and Glucose checks</li>
      </ul>
      <ul class="col-b">
        <li>Personal care and Beauty Products</li>
        <li>Injectables</li>
        <li>Special Orders</li>
        <li>Delivery service</li>
      </ul>
    </div>

    <div class="footer-rule"></div>
    <p class="inquiry">For more inquiries, email us: birchfieldrx@mailhub.com</p>

    <div class="locations">
      <div class="location">
        <div class="line">
          <svg width="9" height="12" viewBox="0 0 9 12" aria-hidden="true"><path d="M4.5 0A4.5 4.5 0 0 0 0 4.5C0 8 4.5 12 4.5 12S9 8 9 4.5A4.5 4.5 0 0 0 4.5 0Zm0 6.3a1.8 1.8 0 1 1 0-3.6 1.8 1.8 0 0 1 0 3.6Z" fill="#1a1a1a"/></svg>
          <span>24 Larkin Street, Port Alder<small>(opposite Greystone Chapel)</small></span>
        </div>
        <div class="line">
          <svg width="12" height="10" viewBox="0 0 12 10" aria-hidden="true"><path d="M1 3C1 1 3 0 6 0s5 1 5 3l-2 1-1-2H4L3 4Z M2 5h8l1 5H1Z" fill="#1a1a1a"/></svg>
          <span>1 555 210 4471</span>
        </div>
        <div class="hours">MONDAY – FRIDAY 10AM TO 6PM<br>SATURDAY 10AM TO 5PM</div>
      </div>
      <div class="location">
        <div class="line">
          <svg width="9" height="12" viewBox="0 0 9 12" aria-hidden="true"><path d="M4.5 0A4.5 4.5 0 0 0 0 4.5C0 8 4.5 12 4.5 12S9 8 9 4.5A4.5 4.5 0 0 0 4.5 0Zm0 6.3a1.8 1.8 0 1 1 0-3.6 1.8 1.8 0 0 1 0 3.6Z" fill="#1a1a1a"/></svg>
          <span>Harbour Walk, Food Court,<br>Port Alder</span>
        </div>
        <div class="line">
          <svg width="12" height="10" viewBox="0 0 12 10" aria-hidden="true"><path d="M1 3C1 1 3 0 6 0s5 1 5 3l-2 1-1-2H4L3 4Z M2 5h8l1 5H1Z" fill="#1a1a1a"/></svg>
          <span>1 555 210 4478</span>
        </div>
        <div class="hours">MONDAY – SATURDAY<br>9AM TO 5PM</div>
      </div>
    </div>

    <div class="social">
      Visit us on
      <div class="social__dot"></div>
      <div class="social__name">Linkora</div>
    </div>
  </section>

  <!-- Corvane Rx Pharmacy ad -->
  <section class="ad ad--corvane" aria-label="Corvane Rx Pharmacy advertisement">
    <div class="hero" role="img" aria-label="Photo of a smiling pharmacist in a white coat reading a medicine label"></div>

    <div class="cv-brand">
      <div class="cv-brand__mark"></div>
      <div>
        <div class="cv-brand__name">Corvane Rx</div>
        <div class="cv-brand__sub">PHARMACY</div>
      </div>
    </div>

    <div class="accept">
      <div class="accept__title">WE ACCEPT:</div>
      <div class="accept__row">
        <span class="payment">Paylane</span>
        <span class="payment">Cardora</span>
        <span class="payment">Sagewell</span>
        <span class="payment">Nortide</span>
      </div>
    </div>

    <svg class="band" width="569" height="140" viewBox="0 0 569 140" aria-hidden="true">
      <path d="M0 38 C150 70 300 80 420 60 C490 48 540 30 569 18 V140 H0 Z" fill="var(--green-pale)"/>
      <path d="M0 30 C150 62 300 72 420 52 C490 40 540 22 569 10 V20 C540 34 490 52 420 64 C300 84 150 74 0 44 Z" fill="var(--green)"/>
      <path d="M0 58 C150 90 300 96 420 78 C490 68 540 52 569 40 V140 H0 Z" fill="var(--green)"/>
      <path d="M0 124 C150 100 420 98 569 120 V140 H0 Z" fill="var(--blue)"/>
      <path d="M0 132 C150 108 420 106 569 128 V140 H0 Z" fill="var(--white)"/>
    </svg>
    <div class="slogan">Where good health begins</div>

    <div class="cv-discounts">
      <div class="cv-discount">
        <span class="cv-discount__rate">10%</span>
        <span class="cv-discount__text"><span class="cv-discount__label">DISCOUNT</span><br><span class="cv-discount__detail">ON SENIOR CITIZEN</span></span>
      </div>
      <div class="cv-discount">
        <span class="cv-discount__rate">10%</span>
        <span class="cv-discount__text"><span class="cv-discount__label">DISCOUNT</span><br><span class="cv-discount__detail">ON STUDENT WITH<br>VALID ID CARD</span></span>
      </div>
      <div class="cv-discount">
        <span class="cv-discount__rate">10%</span>
        <span class="cv-discount__text"><span class="cv-discount__label">DISCOUNT</span><br><span class="cv-discount__detail">ON HOSPITAL<br>PRESCRIPTIONS</span></span>
      </div>
    </div>

    <div class="cv-divider"></div>

    <div class="cv-services">
      <ul class="col-a">
        <li>Certified Pharmacists</li>
        <li>Affordable prices</li>
        <li>Brand and<br>Generic Medicines</li>
        <li>Blood Pressure and<br>Glucose checks</li>
      </ul>
      <ul class="col-b">
        <li>Personal care and<br>Beauty Products</li>
        <li>Injectables</li>
        <li>Special Orders</li>
        <li>Delivery service</li>
      </ul>
    </div>

    <div class="cv-footer">
      <div class="cv-contact">
        <div class="line">
          <svg width="12" height="16" viewBox="0 0 9 12" aria-hidden="true"><path d="M4.5 0A4.5 4.5 0 0 0 0 4.5C0 8 4.5 12 4.5 12S9 8 9 4.5A4.5 4.5 0 0 0 4.5 0Zm0 6.3a1.8 1.8 0 1 1 0-3.6 1.8 1.8 0 0 1 0 3.6Z" fill="#2e4ba0"/></svg>
          <span>Unit B4, Palmcrest Hotel, Shore Road, Port Alder</span>
        </div>
        <div class="line">
          <svg width="16" height="12" viewBox="0 0 16 12" aria-hidden="true"><rect x="0" y="0" width="16" height="12" fill="#2e4ba0"/><path d="M1 1 8 7 15 1" fill="none" stroke="#7cbf43" stroke-width="1.5"/></svg>
          <span>corvanerx@mailhub.com</span>
          <svg class="gap" width="18" height="14" viewBox="0 0 12 10" aria-hidden="true"><path d="M1 3C1 1 3 0 6 0s5 1 5 3l-2 1-1-2H4L3 4Z M2 5h8l1 5H1Z" fill="#2e4ba0"/></svg>
          <span>1 555 318 2290</span>
        </div>
        <div class="cv-hours">MONDAY – SATURDAY 8AM TO 7PM</div>
      </div>
      <div class="cv-social">
        Visit us on
        <div class="social__dot"></div>
        <div class="social__name">Linkora</div>
      </div>
    </div>
  </section>

</div>
</body>
</html>
```